Boutique Sparkling Blanc de Blancs Wine label

We are looking for a label and neck label for our new Sparkling Chardonnay.
Images uploaded include, bubbles and glitter maybe as a faded background for whole label?
We like Refined, elegant yet simple designs.
Have included our current table chardonnay label as example.

Industry/Entity Type

Boutique

Font styles to use
Decorative
Script

Requirements
Must have
• Name - "Every Moonlit Hour"
• Methode Traditionelle
• Blanc de Blancs
• 2015
• Beyond the Orchards (Brand)
• Adelaide Hills
Nice to have
• Neutral tones
• Sparkles, Glitter, Bubbles
• Traditional, cursive or vine like fonts
• Have attached fonts we used for previous wine label - might be nice to carry through same/similar fonts to continue our brand?
Should not have
• a lot of colour

```html
<!DOCTYPE html>
<html lang="en">
<head>
<meta charset="utf-8">
<title>Sparkling Blanc de Blancs Labels</title>
<link href="https://fonts.googleapis.com/css2?family=Kaushan+Script&family=Merriweather:wght@300&display=swap" rel="stylesheet">
<style>
  :root {
    --canvas: #ffffff;
    --label: #ffffff;
    --name: #ffffff;
    --detail: #6f6a66;
    --brand: #2e2a28;
    --amber-core: #ee7a3a;
    --amber-glow: #f7c463;
    --sky-core: #7aaed6;
    --sky-glow: #d6e6f2;
    --claret-core: #9c3f3f;
    --claret-glow: #d99a78;
  }
  html, body {
    margin: 0;
    width: 1200px;
    height: 1001px;
    overflow: hidden;
    background: var(--canvas);
  }
  .label-range {
    display: flex;
    justify-content: space-between;
    align-items: center;
    width: 1050px;
    height: 1001px;
    margin: 0 auto;
  }
  .label {
    position: relative;
    width: 300px;
    height: 440px;
    background: var(--label);
    box-shadow: 0 0 0 1px #eeeeee;
    overflow: hidden;
    text-align: center;
  }
  .label__glow {
    position: absolute;
    inset: 0;
    filter: blur(6px);
  }
  .label--amber .label__glow {
    background:
      radial-gradient(ellipse 46% 22% at 50% 36%, var(--amber-core) 0%, rgba(238,122,58,0.55) 55%, rgba(255,255,255,0) 100%),
      radial-gradient(ellipse 60% 34% at 45% 42%, var(--amber-glow) 0%, rgba(247,196,99,0.4) 50%, rgba(255,255,255,0) 100%),
      radial-gradient(ellipse 45% 30% at 50% 62%, rgba(240,200,170,0.45) 0%, rgba(255,255,255,0) 100%);
  }
  .label--sky .label__glow {
    background:
      radial-gradient(ellipse 40% 22% at 30% 40%, var(--sky-core) 0%, rgba(122,174,214,0.45) 55%, rgba(255,255,255,0) 100%),
      radial-gradient(ellipse 35% 20% at 75% 45%, rgba(122,174,214,0.6) 0%, rgba(255,255,255,0) 100%),
      radial-gradient(ellipse 60% 35% at 50% 45%, var(--sky-glow) 0%, rgba(255,255,255,0) 100%);
  }
  .label--claret .label__glow {
    background:
      radial-gradient(ellipse 45% 24% at 50% 36%, var(--claret-core) 0%, rgba(156,63,63,0.55) 55%, rgba(255,255,255,0) 100%),
      radial-gradient(ellipse 60% 36% at 50% 48%, var(--claret-glow) 0%, rgba(217,154,120,0.35) 50%, rgba(255,255,255,0) 100%),
      radial-gradient(ellipse 50% 30% at 50% 68%, rgba(200,140,150,0.4) 0%, rgba(255,255,255,0) 100%);
  }
  .label__text {
    position: relative;
    padding-top: 84px;
  }
  .label__name {
    margin: 0;
    font-family: "Kaushan Script", cursive;
    font-weight: 400;
    font-size: 96px;
    line-height: 1;
    color: var(--name);
    letter-spacing: -2px;
  }
  .label__details {
    margin: 10px 0 0;
    font-family: "Merriweather", serif;
    font-weight: 300;
    font-size: 13px;
    line-height: 16px;
    color: var(--detail);
  }
  .label__brand {
    margin: 16px 0 0;
    font-family: "Merriweather", serif;
    font-weight: 300;
    font-size: 17px;
    color: var(--brand);
  }
  .label__region {
    margin: 8px 0 0;
    font-family: "Merriweather", serif;
    font-weight: 300;
    font-size: 13px;
    color: var(--detail);
  }
</style>
</head>
<body>
<main class="label-range">
  <section class="label label--amber">
    <div class="label__glow" role="img" aria-label="Soft orange and gold sparkling bokeh background"></div>
    <div class="label__text">
      <h1 class="label__name">Name</h1>
      <p class="label__details">Methode Traditionelle<br>Blanc de Blancs<br>2015</p>
      <p class="label__brand">Beyond the Orchards</p>
      <p class="label__region">Adelaide Hills</p>
    </div>
  </section>
  <section class="label label--sky">
    <div class="label__glow" role="img" aria-label="Soft pale blue sparkling bokeh background"></div>
    <div class="label__text">
      <h1 class="label__name">Name</h1>
      <p class="label__details">Methode Traditionelle<br>Blanc de Blancs<br>2015</p>
      <p class="label__brand">Beyond the Orchards</p>
      <p class="label__region">Adelaide Hills</p>
    </div>
  </section>
  <section class="label label--claret">
    <div class="label__glow" role="img" aria-label="Soft claret and rose sparkling bokeh background"></div>
    <div class="label__text">
      <h1 class="label__name">Name</h1>
      <p class="label__details">Methode Traditionelle<br>Blanc de Blancs<br>2015</p>
      <p class="label__brand">Beyond the Orchards</p>
      <p class="label__region">Adelaide Hills</p>
    </div>
  </section>
</main>
</body>
</html>
```